Grand Opening for Brightvale Church

Would like to have a BillBoard Created according to the specs listed by the company who will be producing the print. I am attaching the spec sheet to this post. I am also attaching a couple different picture options as well as a former Billboard design that was done. I would like the design to incorporate my logo, picture. I am okay if the background on the picture is eliminated for creative purposes. The words to be displayed is "Grand Opening" April 12, 2020 at the former Halden Middle School) 71st Marsh Hollow Rd.

Colors

Designer to choose colors to be used in the design.

Requirements
Must have
• Something that pops
Nice to have
• Good color coordinations and clearly visible text

```html
<!DOCTYPE html>
<html lang="en">
<head>
<meta charset="utf-8">
<title>Brightvale Church – Grand Opening Billboard</title>
<link href="https://fonts.googleapis.com/css2?family=Montserrat:wght@600;700;800&display=swap" rel="stylesheet">
<style>
  :root {
    --page: #ffffff;
    --board-deep: #1c0202;
    --board-mid: #3a0505;
    --glow-red: #b3200e;
    --glow-orange: #f07a2a;
    --badge-fill: #5e0404;
    --gold: #d9a441;
    --gold-light: #f3d27a;
    --text: #ffffff;
    --photo-dark: #5a2a14;
    --photo-mid: #a4572a;
    --photo-light: #d9b9a3;
  }
  * { margin: 0; padding: 0; box-sizing: border-box; }
  html, body {
    width: 1200px; height: 1000px; overflow: hidden;
    background: var(--page);
    font-family: "Montserrat", Arial, sans-serif;
  }
  .billboard {
    position: absolute;
    left: 100px; top: 244px;
    width: 998px; height: 497px;
    overflow: hidden;
    background:
      radial-gradient(ellipse 520px 160px at 92% 58%, rgba(240,122,42,0.75), rgba(179,32,14,0.35) 45%, transparent 75%),
      radial-gradient(ellipse 700px 260px at 80% 40%, rgba(179,32,14,0.45), transparent 70%),
      linear-gradient(100deg, var(--board-deep) 0%, var(--board-deep) 35%, var(--board-mid) 70%, #4a0804 100%);
    color: var(--text);
  }
  .church-name {
    position: absolute;
    left: 150px; top: 70px;
    width: 360px;
    text-align: center;
    font-weight: 700;
    font-size: 46px;
    line-height: 1.1;
    color: var(--text);
  }
  .church-name .dot {
    display: inline-block;
    width: 18px; height: 18px;
    border-radius: 50%;
    background: var(--glow-orange);
    margin-right: 12px;
    vertical-align: middle;
  }
  .grand-badge {
    position: absolute;
    left: 180px; top: 249px;
    width: 297px; height: 96px;
    border: 3px solid var(--gold);
    background: linear-gradient(var(--gold-light), var(--gold));
    padding: 6px;
  }
  .grand-badge span {
    display: flex; align-items: center; justify-content: center;
    width: 100%; height: 100%;
    background: var(--badge-fill);
    font-weight: 800;
    font-size: 56px;
    letter-spacing: 1px;
    text-shadow: 2px 3px 4px rgba(0,0,0,0.5);
  }
  .opening {
    position: absolute;
    left: 180px; top: 360px;
    width: 297px;
    text-align: center;
    font-weight: 700;
    font-size: 22px;
    letter-spacing: 15px;
    padding-left: 15px;
  }
  .event-details {
    position: absolute;
    left: 60px; top: 404px;
    width: 540px;
    text-align: center;
    font-weight: 700;
    font-size: 16.5px;
    line-height: 25px;
    text-transform: uppercase;
  }
  .speaker-photo {
    position: absolute;
    left: 565px; top: 66px;
    width: 330px; height: 431px;
    border-radius: 120px 120px 0 0;
    background:
      linear-gradient(180deg, var(--photo-light) 0%, var(--photo-mid) 35%, var(--photo-dark) 100%);
    opacity: 0.9;
  }
</style>
</head>
<body>
  <section class="billboard">
    <h1 class="church-name"><span class="dot"></span>Brightvale Church</h1>
    <div class="grand-badge"><span>GRAND</span></div>
    <p class="opening">OPENING</p>
    <p class="event-details">April 12, 2020 at the former<br>Halden Middle School. 71st Marsh Hollow Rd.</p>
    <div class="speaker-photo" role="img" aria-label="Photo of the pastor in a rust-coloured blazer, speaking with open hands"></div>
  </section>
</body>
</html>
```